Realty Group Needs Classy, Contemporary Letterhead Design

We need a letterhead design for a new realty company located in NY, USA. We buy investment properties to rehabilitate and or keep in our rental portfolio.

```html
<!DOCTYPE html>
<html lang="en">
<head>
<meta charset="utf-8">
<title>Meridale Realty Group – Letterhead</title>
<link rel="stylesheet" href="https://fonts.googleapis.com/css2?family=Open+Sans:wght@400;700&family=Montserrat:wght@800&display=swap">
<style>
  :root {
    --backdrop: #e8e8ea;
    --paper: #ffffff;
    --brand-purple: #4a2382;
    --rule-grey: #b9b9bd;
    --footer-text: #ffffff;
    --icon-dot: #7fae5a;
  }
  * { margin: 0; padding: 0; box-sizing: border-box; }
  html, body {
    width: 1200px;
    height: 795px;
    overflow: hidden;
    background: var(--backdrop);
  }
  .letterhead {
    position: absolute;
    left: 340px;
    top: 30px;
    width: 520px;
    height: 735px;
    background: var(--paper);
    box-shadow: 0 6px 18px rgba(0,0,0,0.12);
    overflow: hidden;
  }
  .letterhead__shapes {
    position: absolute;
    inset: 0;
  }
  .brand {
    position: absolute;
    left: 46px;
    top: 70px;
    color: var(--brand-purple);
    font-family: "Montserrat", sans-serif;
    font-weight: 800;
    line-height: 1;
  }
  .brand__name {
    font-size: 30px;
    letter-spacing: 0.5px;
    display: block;
  }
  .brand__tagline {
    display: block;
    font-size: 10px;
    margin-top: 4px;
    text-align: right;
    letter-spacing: 0.4px;
  }
  .contact {
    position: absolute;
    right: 22px;
    bottom: 20px;
    color: var(--footer-text);
    font-family: "Open Sans", sans-serif;
    font-style: normal;
    font-size: 8.5px;
    line-height: 14px;
    text-align: right;
  }
  .contact__company,
  .contact__web { font-weight: 700; }
  .contact__company { font-size: 9.5px; }
  .contact__line {
    display: flex;
    justify-content: flex-end;
    align-items: center;
    gap: 4px;
  }
  .contact__icon {
    width: 7px;
    height: 7px;
    border-radius: 50%;
    background: var(--icon-dot);
    margin-left: 6px;
  }
  .contact__icon:first-child { margin-left: 0; }
</style>
</head>
<body>
  <main class="letterhead">
    <svg class="letterhead__shapes" viewBox="0 0 520 735" width="520" height="735" aria-hidden="true">
      <defs>
        <linearGradient id="header-wash" x1="0" y1="0" x2="0" y2="1">
          <stop offset="0" stop-color="#f4f4f6"/>
          <stop offset="1" stop-color="#e6e6e9"/>
        </linearGradient>
      </defs>
      <path d="M0 0 H420 Q330 190 0 235 Z" fill="url(#header-wash)"/>
      <path d="M0 724 Q180 713 520 458" fill="none" stroke="var(--rule-grey)" stroke-width="3"/>
      <path d="M0 735 Q180 725 520 470 V735 Z" fill="var(--brand-purple)"/>
    </svg>

    <div class="brand">
      <span class="brand__name">MERIDALE</span>
      <span class="brand__tagline">Realty Group, LLC</span>
    </div>

    <address class="contact">
      <div class="contact__company">Meridale Realty Group, LLC</div>
      <div>Suite 102 Street name, State, Zip 2034, Country</div>
      <div class="contact__line">
        <span class="contact__icon"></span><span>(00) 01234 567 890</span>
        <span class="contact__icon"></span><span>(00) 01234 567 891</span>
        <span class="contact__icon"></span><span>hello@meridalerealty.com</span>
      </div>
      <div class="contact__web">www.meridalerealtygroup.com</div>
    </address>
  </main>
</body>
</html>
```